New business needs a slick but classy, conservative and elegant Legal Letterhead

We need a new letterhead for a law firm that is slick but very classy and also understated.

The name of the firm is K.L. Marlow Lawyers.

All information about the Law firm should appear at the top of the page. Please no firm information in the footer.

It should have a clean, neat look. No watermarks or bold graphics please.

Info should include the name of the law firm, both the street address and postal address, the phone number and the fax number, the names of the principals, the website. We have attached a word document that contains the relevant information.

We have attached a copy of the business card for further information purposes.

We also need a law society logo to appear (probably on the bottom right hand side of the letterhead?) that states our affiliation to the law society. It is attached and must not be altered in any way. It can be small.

The only footer text we require is as worded in the attached information document.

We would like to see designs that use red and white - in an understated, elegant style - not too modern or too gaudy looking.

The final design should communicate that we mean business and that we are to be trusted.
Updates

Please insert firm's name K.L. Marlow Lawyers on letterhead! I have removed KLM logo as designers were using it instead of the name of the firm. Thank you!

Industry/Entity Type

Legal

Font styles to use
Serif

Colors
ec1f27
ffffff

Requirements
Must have
• All information contained in the word document attached - firm details, law society affiliation logo, firm name & firm logo, principals' names.
Should not have
• watermarks
• no firm details in footer

```html
<!DOCTYPE html>
<html lang="en">
<head>
<meta charset="utf-8">
<title>K.L. Marlow Lawyers – Letterhead</title>
<link rel="stylesheet" href="https://fonts.googleapis.com/css2?family=Noto+Sans:wght@400;700&family=Tinos&display=swap">
<style>
  :root {
    --brand-red: #ec1f27;
    --ink: #333333;
    --paper: #ffffff;
  }
  * { margin: 0; padding: 0; box-sizing: border-box; }
  html, body { width: 849px; height: 1200px; overflow: hidden; background: var(--paper); }
  .letterhead {
    position: relative;
    width: 849px;
    height: 1200px;
    background: var(--paper);
    font-family: "Noto Sans", Verdana, sans-serif;
    color: var(--ink);
  }
  .top-rule {
    position: absolute; left: 0; top: 0;
    width: 595px; height: 10px;
    background: var(--brand-red);
  }
  .firm-name {
    position: absolute; left: 28px; top: 30px;
    font-size: 39px; font-weight: 700; letter-spacing: 0.5px;
    color: var(--brand-red);
    line-height: 1;
  }
  .principals {
    position: absolute; left: 28px; top: 80px;
    font-size: 16px; font-weight: 700;
    color: var(--brand-red);
  }
  .contact {
    position: absolute; right: 26px; top: 28px;
    list-style: none;
    text-align: right;
    font-size: 12.5px;
    line-height: 20px;
  }
  .contact li { display: flex; justify-content: flex-end; align-items: center; gap: 6px; }
  .contact svg { width: 14px; height: 14px; flex: none; }
  .contact .website { color: var(--brand-red); margin-top: 6px; padding-right: 20px; }
  .side-band {
    position: absolute; right: 0; top: 192px;
    width: 25px; height: 983px;
    background: var(--brand-red);
  }
  .side-band::before {
    content: ""; position: absolute; left: -6px; top: 0;
    width: 4px; height: 16px; background: var(--brand-red);
  }
  .affiliation-badge {
    position: absolute; left: 28px; top: 1095px;
    width: 26px; height: 36px;
    background: var(--brand-red);
    border-radius: 2px 2px 13px 13px;
  }
  .footer-rule {
    position: absolute; left: 28px; top: 1143px;
    width: 354px; height: 2px;
    background: var(--brand-red);
  }
  .footer-note {
    position: absolute; left: 28px; top: 1152px;
    font-family: "Tinos", "Times New Roman", serif;
    font-size: 11px;
    color: var(--ink);
  }
</style>
</head>
<body>
<main class="letterhead">
  <div class="top-rule"></div>

  <header>
    <h1 class="firm-name">K.L. MARLOW LAWYERS</h1>
    <p class="principals">Principals: Karen Marlow &amp; Lewis Marlow</p>

    <ul class="contact">
      <li>Shop 4, 18-36 Hartley Circuit Ashbury Park&nbsp; NSW&nbsp; 2214
        <svg viewBox="0 0 14 14" aria-hidden="true"><path d="M1 7 7 1.5 13 7h-2v5.5H8.5V9h-3v3.5H3V7z" fill="#ec1f27"/></svg>
      </li>
      <li>PO Box 5127 Ashbury Park&nbsp; NSW&nbsp; 2214
        <svg viewBox="0 0 14 14" aria-hidden="true"><rect x="2" y="3" width="10" height="6" rx="3" fill="#ec1f27"/><rect x="6.2" y="9" width="1.6" height="4.5" fill="#ec1f27"/></svg>
      </li>
      <li>(02) 9000 4812
        <svg viewBox="0 0 14 14" aria-hidden="true"><path d="M2 3.5C2 2 4.5 1.5 7 1.5S12 2 12 3.5V5H9.5V4h-5v1H2zM3 6h8l1 6.5H2z" fill="#ec1f27"/><circle cx="7" cy="9" r="1.6" fill="#fff"/></svg>
      </li>
      <li>(02) 9000 4813
        <svg viewBox="0 0 14 14" aria-hidden="true"><rect x="3.5" y="1" width="7" height="4" fill="#ec1f27"/><rect x="1.5" y="5.5" width="11" height="7" rx="1" fill="#ec1f27"/><rect x="4" y="8" width="6" height="1.3" fill="#fff"/></svg>
      </li>
      <li class="website">www.klmarlow.com.au</li>
    </ul>
  </header>

  <div class="side-band"></div>

  <footer>
    <div class="affiliation-badge" role="img" aria-label="Law society affiliation badge"></div>
    <div class="footer-rule"></div>
    <p class="footer-note">Liability limited by a scheme approved under Professional Standards Legislation</p>
  </footer>
</main>
</body>
</html>
```